Web design for a Crane & Heavy Equipment Inspection, Repair and Maintenance Company in Texas

We need a web design for a new company based in Houston, Texas called "Bristen Hoist & Equipment". We inspect, repair and maintain diesel driven heavy equipment, generators, fire water pumps and cranes. We would like to see designs that use the colors orange, white, yellow and brown, and/or orange, white, navy, yellow and grey.

```html
<!DOCTYPE html>
<html lang="en">
<head>
<meta charset="utf-8">
<title>Bristen Hoist &amp; Equipment</title>
<link rel="stylesheet" href="https://fonts.googleapis.com/css2?family=Open+Sans:wght@300;400;600&display=swap">
<style>
  :root {
    --navy: #0f3d6e;
    --orange: #f15a24;
    --white: #ffffff;
    --heading: #555a60;
    --body: #a0a4a8;
    --hero-dark: #3a2a22;
    --hero-warm: #b9794a;
  }
  * { margin: 0; padding: 0; box-sizing: border-box; }
  html, body { width: 930px; height: 1200px; overflow: hidden; }
  body { font-family: "Open Sans", sans-serif; background: var(--white); position: relative; }

  .site-header { position: absolute; top: 0; left: 0; width: 930px; height: 107px; background: var(--navy); }
  .brand { position: absolute; left: 125px; top: 38px; color: var(--white); font-size: 17px; font-weight: 600; letter-spacing: .3px; }
  .brand-mark { display: inline-block; width: 10px; height: 10px; background: var(--orange); margin-right: 7px; vertical-align: 1px; }
  .main-nav { position: absolute; top: 49px; right: 125px; display: flex; gap: 23px; }
  .main-nav a, .footer-nav a { color: var(--white); text-decoration: none; font-size: 8.5px; text-transform: uppercase; }
  .main-nav a.active, .footer-nav a.active { color: var(--orange); }

  .hero { position: absolute; top: 107px; left: 0; width: 930px; height: 378px;
    background: linear-gradient(180deg, #6e5446 0%, var(--hero-warm) 55%, #6a4a34 78%, var(--hero-dark) 100%); }
  .hero-title { position: absolute; left: 125px; top: 82px; font-size: 24px; font-weight: 600; color: var(--white); }
  .hero-title span { color: var(--orange); }
  .hero-text { position: absolute; left: 125px; top: 133px; width: 322px; color: var(--white); font-size: 9.6px; font-weight: 600; line-height: 14px; }
  .hero-text p + p { margin-top: 14px; }
  .slider-arrow { position: absolute; top: 177px; width: 24px; height: 24px; background: rgba(255,255,255,.25); }
  .slider-arrow.prev { left: 42px; } .slider-arrow.next { left: 862px; }
  .slider-arrow svg { display: block; }
  .slider-dots { position: absolute; left: 372px; top: 365px; display: flex; gap: 1px; }
  .slider-dots i { width: 61px; height: 2px; background: rgba(255,255,255,.45); }
  .slider-dots i.current { background: var(--white); }

  .section-title { position: absolute; left: 0; width: 930px; text-align: center; font-size: 16px; font-weight: 600; color: var(--heading); }
  .section-title .accent { color: var(--orange); } .section-title .navy { color: var(--navy); }
  .welcome-text { position: absolute; left: 125px; top: 568px; width: 680px; text-align: center; color: var(--body); font-size: 9.6px; font-weight: 300; line-height: 14px; }
  .welcome-text p + p { margin-top: 14px; }
  .btn { position: absolute; display: block; height: 19px; line-height: 19px; text-align: center; color: var(--white); font-size: 8px; text-decoration: none; }
  .btn.navy { background: var(--navy); } .btn.orange { background: var(--orange); }

  .service { position: absolute; top: 800px; width: 215px; text-align: center; }
  .service-photo { width: 215px; height: 114px; }
  .service h3 { margin-top: 11px; font-size: 12px; font-weight: 600; color: var(--heading); }
  .service p { margin-top: 9px; font-size: 9.6px; font-weight: 300; color: var(--body); line-height: 14px; }
  .service .btn { position: static; width: 58px; margin: 16px auto 0; }

  .site-footer { position: absolute; top: 1106px; left: 0; width: 930px; height: 94px; background: var(--navy); }
  .footer-nav { position: absolute; left: 125px; top: 35px; display: flex; gap: 23px; }
  .social { position: absolute; left: 718px; top: 28px; display: flex; gap: 10px; }
  .social span { width: 22px; height: 22px; border: 1px solid var(--orange); }
  .copyright { position: absolute; left: 125px; top: 76px; color: var(--white); font-size: 7.5px; }
</style>
</head>
<body>
  <header class="site-header">
    <div class="brand"><span class="brand-mark"></span>Bristen Hoist &amp; Equipment</div>
    <nav class="main-nav">
      <a class="active" href="#">Home</a><a href="#">About Us</a><a href="#">Services</a><a href="#">Our Partners</a><a href="#">Why Choose Us</a><a href="#">Contact Us</a>
    </nav>
  </header>

  <section class="hero" role="img" aria-label="Harbour cranes and a cargo ship at sunset">
    <h1 class="hero-title"><span>BRISTEN</span> HOIST &amp; EQUIPMENT</h1>
    <div class="hero-text">
      <p>Lorem ipsum dolor sit amet, consectetur adipiscing elit. Mauris bibendum diam sapien, nec tristique tellus condimentum quis. Curabitur ut ipsum neque. Donec ultricies sollicitudin eros, at condimentum tellus vestibulum a. Morbi dapibus arcu eget justo pharetra dapibus.</p>
      <p>Curabitur ornare nisi sed nibh dapibus scelerisque. Etiam augue turpis, imperdiet fringilla vulputate id, cursus sit amet lorem. In viverra lacus metus. Integer bibendum vitae lorem vel fermentum.</p>
    </div>
    <div class="slider-arrow prev"><svg width="24" height="24"><path d="M14 7 L9 12 L14 17" fill="none" stroke="#fff" stroke-width="1.5"/></svg></div>
    <div class="slider-arrow next"><svg width="24" height="24"><path d="M10 7 L15 12 L10 17" fill="none" stroke="#fff" stroke-width="1.5"/></svg></div>
    <div class="slider-dots"><i class="current"></i><i></i><i></i></div>
  </section>

  <h2 class="section-title" style="top:526px">WELCOME TO <span class="accent">BRISTEN</span> <span class="navy">HOIST</span></h2>
  <div class="welcome-text">
    <p>Lorem ipsum dolor sit amet, consectetur adipiscing elit. Mauris bibendum diam sapien, nec tristique tellus condimentum quis. Curabitur ut ipsum neque. Donec ultricies sollicitudin eros, at condimentum tellus vestibulum a. Morbi dapibus arcu eget justo pharetra dapibus. Curabitur ornare nisi sed nibh dapibus scelerisque. Etiam augue turpis, imperdiet fringilla vulputate id, cursus sit amet lorem.</p>
    <p>In viverra lacus metus. Integer bibendum vitae lorem vel fermentum. Donec eget feugiat leo. Phasellus commodo tincidunt ornare.<br>Vestibulum fermentum rhoncus fringilla.</p>
  </div>
  <a class="btn navy" href="#" style="left:436px;top:672px;width:58px">READ MORE</a>

  <h2 class="section-title" style="top:755px">OUR SERVICES</h2>

  <article class="service" style="left:125px">
    <div class="service-photo" role="img" aria-label="Technician inspecting a red crane component" style="background:linear-gradient(135deg,#2c3e5c,#5a6e8a 50%,#a8404a)"></div>
    <h3>Inspection</h3>
    <p>Lorem ipsum dolor sit amet, consectetur adipiscing elit. Mauris bibendum diam sapien, nec tristique tellus condimentum quis</p>
    <a class="btn orange" href="#">READ MORE</a>
  </article>
  <article class="service" style="left:358px">
    <div class="service-photo" role="img" aria-label="Engineer servicing an electrical control panel" style="background:linear-gradient(135deg,#3a3a3a,#6f6a5a 50%,#c9a640)"></div>
    <h3>Maintenance</h3>
    <p>Lorem ipsum dolor sit amet, consectetur adipiscing elit. Mauris bibendum diam sapien, nec tristique tellus condimentum quis</p>
    <a class="btn orange" href="#">READ MORE</a>
  </article>
  <article class="service" style="left:590px">
    <div class="service-photo" role="img" aria-label="Workers repairing a large industrial motor" style="background:linear-gradient(135deg,#2f6f9a,#4a5866 50%,#b8743a)"></div>
    <h3>Repairment</h3>
    <p>Lorem ipsum dolor sit amet, consectetur adipiscing elit. Mauris bibendum diam sapien, nec tristique tellus condimentum quis</p>
    <a class="btn orange" href="#">READ MORE</a>
  </article>

  <footer class="site-footer">
    <nav class="footer-nav">
      <a class="active" href="#">Home</a><a href="#">About Us</a><a href="#">Services</a><a href="#">Our Partners</a><a href="#">Why Choose Us</a><a href="#">Contact Us</a>
    </nav>
    <div class="social"><span></span><span></span><span></span></div>
    <p class="copyright">Copyright © 2014 BRISTEN HOIST - All Rights Reserved.</p>
  </footer>
</body>
</html>
```